Business Card template designs

We need a lot of Business card designs.
Your designs will get exposure on our newly opened business-card printing website.
We are committed to quality of paper and packages we use, so they will come up very fancy.

Here is your advantage. We will put the profile of the graphic designer on our site so that you can showcase your designs to people around the world and in Japan.

A profile is not mandatory, although we encourage graphic designers to have a profile to get continuous work in the future.
We are looking forward to having many good designs.

The right of the use of design will be owned by us.
The design may be used to the products other than
business cards.

Target Market(s)

designer,photographer,creator,artist

Industry/Entity Type

Printing

Contact Information for Business Card

The back design is important.
Please check the reference file.

Requirements
Must have
• Please include the following, required information on your business card designs.
• Name: Haruna Okabe
• Title: Designer
• Web: https://www.ketori.co.jp/kt/
• Address: 4-17 Kamiharuta-Cho Meguro-ku, Tokyo
• Email: info@kketori.com
• Phone: 03 4816 3907
• Mobile: 070 2143 6658
• * For Japanese sites, we will convert the text portion to Japanese characters.
• * In case of 28mmx70mm only include Name,Enail,Phone and SNS account(https://www.facebook.com/kketori.com)
• 1. colorful
• 2. simple
• 3. natural
• 4. modern
• 5. cool
• 6. sporty
• Please make variations of the same image with 3-6
• different colors / patterns for one design so that
• customers can compare and choose.
• If you want to use a same picture, please make make
• copies and paste on each different types of design.
Nice to have
• You may also use, the following non-required information.
• Company Name: Ketori, Inc.
• Fax: 03-4173-9620
• Open space for company logo

```html
<!DOCTYPE html>
<html lang="en">
<head>
<meta charset="utf-8">
<title>Business Card – Haruna Okabe</title>
<link rel="stylesheet" href="https://fonts.googleapis.com/css2?family=Sorts+Mill+Goudy&family=PT+Sans&display=swap">
<style>
  :root {
    --backdrop: #e6e3df;
    --card-light: #f4f4f4;
    --card-dark: #0b0b0b;
    --ink: #111111;
    --ink-soft: #2a2a2a;
    --paper-white: #ffffff;
  }
  * { margin: 0; padding: 0; box-sizing: border-box; }
  html, body {
    width: 1200px;
    height: 900px;
    overflow: hidden;
    background: var(--backdrop);
  }
  .canvas {
    position: relative;
    width: 1200px;
    height: 900px;
  }
  .card {
    position: absolute;
    border-radius: 30px;
    box-shadow: 0 6px 18px rgba(0, 0, 0, 0.12);
  }
  .card--front {
    left: 298px;
    top: 60px;
    width: 559px;
    height: 345px;
    background: var(--card-light);
    color: var(--ink);
  }
  .card--back {
    left: 416px;
    top: 519px;
    width: 556px;
    height: 343px;
    background: var(--card-dark);
    color: var(--paper-white);
  }
  .logo-placeholder {
    position: absolute;
    font-family: "Sorts Mill Goudy", Georgia, serif;
    font-size: 82px;
    line-height: 70px;
    letter-spacing: -1px;
  }
  .card--front .logo-placeholder { left: 46px; top: 108px; }
  .card--back .logo-placeholder { left: 171px; top: 100px; }
  .logo-placeholder span { display: block; }

  .identity {
    position: absolute;
    left: 306px;
    top: 68px;
  }
  .identity__name {
    font-family: "Sorts Mill Goudy", Georgia, serif;
    font-size: 27px;
    font-weight: 700;
    line-height: 32px;
    -webkit-text-stroke: 0.4px var(--ink);
  }
  .identity__title {
    font-family: "Sorts Mill Goudy", Georgia, serif;
    font-size: 17px;
    line-height: 20px;
    color: var(--ink-soft);
    letter-spacing: 0.5px;
  }
  .contacts {
    list-style: none;
    margin-top: 15px;
    font-family: "PT Sans", Arial, sans-serif;
    font-size: 15.5px;
    line-height: 21.5px;
  }
  .contacts li {
    display: flex;
    align-items: center;
    gap: 9px;
  }
  .contacts svg {
    width: 12px;
    height: 12px;
    flex: none;
    fill: var(--ink);
  }
  .address {
    margin-top: 11px;
    font-family: "PT Sans", Arial, sans-serif;
    font-style: normal;
    font-size: 15.5px;
    line-height: 21.5px;
  }
</style>
</head>
<body>
<main class="canvas">
  <section class="card card--front" aria-label="Business card front">
    <div class="logo-placeholder"><span>Logo</span><span>Here</span></div>
    <div class="identity">
      <h1 class="identity__name">Haruna Okabe</h1>
      <p class="identity__title">Designer</p>
      <ul class="contacts">
        <li>
          <svg viewBox="0 0 12 12" aria-hidden="true"><path d="M1 4.2C1 2.5 3.2 1.6 6 1.6s5 .9 5 2.6v.9H8.6v-1H3.4v1H1z M3 5.6h6l1.6 4.4H1.4z M6 6.6a1.3 1.3 0 1 0 0 2.6 1.3 1.3 0 0 0 0-2.6z"/></svg>
          <span>03 4816 3907</span>
        </li>
        <li>
          <svg viewBox="0 0 12 12" aria-hidden="true"><path d="M3.5 0.5h5a.8.8 0 0 1 .8.8v9.4a.8.8 0 0 1-.8.8h-5a.8.8 0 0 1-.8-.8V1.3a.8.8 0 0 1 .8-.8zM3.8 1.8v7.2h4.4V1.8zM6 9.6a.6.6 0 1 0 0 1.2.6.6 0 0 0 0-1.2z"/></svg>
          <span>070 2143 6658</span>
        </li>
        <li>
          <svg viewBox="0 0 12 12" aria-hidden="true"><path d="M1 2.5h10v.6L6 6.6 1 3.1z M1 4.3l5 3.5 5-3.5v5.2H1z"/></svg>
          <span>Email: info@kketori.com</span>
        </li>
        <li>
          <svg viewBox="0 0 12 12" aria-hidden="true"><circle cx="6" cy="6" r="5.4"/><path d="M3.2 3.4c1 .2 1.6.9 1.4 1.7-.3.8.6 1.2.6 2 0 .7-.5 1.1-.3 1.8M8.4 2.6c-.6.6-.3 1.4.4 1.6.8.2 1 1.1.5 1.7" stroke="#f4f4f4" stroke-width="0.9" fill="none"/></svg>
          <span>www.ketori.co.jp/kt/</span>
        </li>
      </ul>
      <address class="address">4-17 Kamiharuta-Cho<br>Meguro-ku, Tokyo</address>
    </div>
  </section>

  <section class="card card--back" aria-label="Business card back">
    <div class="logo-placeholder"><span>Logo</span><span>Here</span></div>
  </section>
</main>
</body>
</html>
```